Engineering Consultant Business Card

I'm starting a new business as a high-end engineering consultant in a niche field. I've attached the jpg for my logo plus the branding guideline document that I've been following. You can see my business website here: www.tarvikworks.com
I'd like a business card that has the logo on one side, then the other side has (in any order): Tarvik Works, Inc.
Dana Whitlock
President and Chief EMC Engineer
www.tarvikworks.com
dana@tarvikworks.com
Optional: motto "We will solve your EMC problems as early as possible—ideally before they even start."
I'm not planning on including a phone number
Target Market(s)
Businesses, especially makers of electronics hardware
Industry/Entity Type
Electrical engineering
Contact Information for Business Card
Company name, my name, website, email

```html
<!DOCTYPE html>
<html lang="en">
<head>
<meta charset="UTF-8">
<title>Tarvik Works, Inc. — Business Card</title>
<link rel="stylesheet" href="https://fonts.googleapis.com/css2?family=Montserrat:wght@600;700&family=Open+Sans:wght@400;600&display=swap">
<style>
  :root {
    --backdrop: #e4e4e4;
    --card-white: #f7f7f7;
    --brand-blue: #2e3f9f;
    --brand-blue-deep: #263790;
    --divider: #9a9a9a;
    --ink: #2a2a2a;
    --white: #ffffff;
  }
  * { margin: 0; padding: 0; box-sizing: border-box; }
  html, body {
    width: 1200px;
    height: 675px;
    overflow: hidden;
    background: var(--backdrop);
  }
  .stage {
    width: 1200px;
    height: 675px;
    display: flex;
    align-items: center;
    justify-content: center;
    gap: 70px;
  }
  .card {
    width: 500px;
    height: 286px;
    border-radius: 16px;
    box-shadow: 0 6px 18px rgba(0, 0, 0, 0.14);
    position: relative;
    overflow: hidden;
  }
  /* Front side */
  .card-front {
    background: var(--card-white);
    display: flex;
    align-items: center;
    padding: 0 30px 0 34px;
  }
  .front-mark {
    width: 178px;
    display: flex;
    align-items: center;
    gap: 9px;
  }
  .mark-dot {
    width: 30px;
    height: 30px;
    border-radius: 50%;
    border: 4px solid var(--brand-blue);
    flex-shrink: 0;
  }
  .mark-name {
    font-family: "Montserrat", sans-serif;
    font-weight: 700;
    font-size: 21px;
    line-height: 1.1;
    color: var(--brand-blue);
  }
  .front-divider {
    width: 2px;
    height: 116px;
    background: var(--divider);
    margin: 0 18px 0 12px;
    flex-shrink: 0;
  }
  .front-details { display: flex; flex-direction: column; }
  .company-name, .person-name {
    font-family: "Montserrat", sans-serif;
    font-weight: 600;
    font-size: 18px;
    line-height: 1.15;
    color: var(--brand-blue);
  }
  .person-name { text-transform: uppercase; }
  .person-title {
    font-family: "Open Sans", sans-serif;
    font-weight: 600;
    font-size: 8.5px;
    color: var(--ink);
    margin: 3px 0 12px;
  }
  .contact-line {
    display: flex;
    align-items: center;
    gap: 7px;
    font-family: "Open Sans", sans-serif;
    font-size: 13px;
    color: var(--ink);
    line-height: 1.45;
  }
  .contact-icon { width: 10px; height: 10px; flex-shrink: 0; }
  /* Back side */
  .card-back {
    background: linear-gradient(160deg, #3a4daa 0%, var(--brand-blue-deep) 100%);
    display: flex;
    align-items: center;
    justify-content: center;
    gap: 14px;
  }
  .back-dot {
    width: 46px;
    height: 46px;
    border-radius: 50%;
    border: 6px solid var(--white);
  }
  .back-name {
    font-family: "Montserrat", sans-serif;
    font-weight: 700;
    font-size: 34px;
    color: var(--white);
  }
</style>
</head>
<body>
  <main class="stage">
    <section class="card card-front" aria-label="Business card front">
      <div class="front-mark">
        <span class="mark-dot"></span>
        <span class="mark-name">Tarvik<br>Works</span>
      </div>
      <div class="front-divider"></div>
      <div class="front-details">
        <p class="company-name">Tarvik Works, Inc.</p>
        <p class="person-name">Dana Whitlock</p>
        <p class="person-title">President and Chief EMC Engineer</p>
        <p class="contact-line">
          <svg class="contact-icon" viewBox="0 0 10 10" aria-hidden="true">
            <circle cx="5" cy="5" r="5" fill="var(--brand-blue)"/>
            <ellipse cx="5" cy="5" rx="2" ry="3.6" fill="none" stroke="#fff" stroke-width="0.8"/>
            <line x1="1.4" y1="5" x2="8.6" y2="5" stroke="#fff" stroke-width="0.8"/>
          </svg>
          www.tarvikworks.com
        </p>
        <p class="contact-line">
          <svg class="contact-icon" viewBox="0 0 10 10" aria-hidden="true">
            <circle cx="5" cy="5" r="5" fill="var(--brand-blue)"/>
            <rect x="2.2" y="3" width="5.6" height="4" fill="none" stroke="#fff" stroke-width="0.8"/>
            <polyline points="2.2,3 5,5.2 7.8,3" fill="none" stroke="#fff" stroke-width="0.8"/>
          </svg>
          dana@tarvikworks.com
        </p>
      </div>
    </section>
    <section class="card card-back" aria-label="Business card back">
      <span class="back-dot"></span>
      <span class="back-name">Tarvik Works</span>
    </section>
  </main>
</body>
</html>
```